Escape Room Flyer Design - Start up. A5

Flyer is for letterbox drops to get interest and let people know that our business exists and to a lesser extent what an escape room is. We have 1 room (the miller's shadows) and a second room coming soon (Varuna's Vault). I have attached our logo and 2 flyers that I have seen in the past that I really like the design of.
Whether you are having a night out with friends or family, celebrating a special event, planning a team-building activity, or simply wanting a diversion from the doldrums of your workweek, The Lock Box will provide you an unforgettable live-action gaming experience.

Target Market(s)

18-25

Industry/Entity Type

Entertainment

Requirements
Must have
• Logo. Phone number 0417 265 839. Website. www.thelockboxhartwell.com
Bookings essential.
Nice to have
• Mystery, a little bit on the darker side than bright colourful and blocky.
"Many Will Enter…Few Will Escape" tag line
60 minute game. Team work. 2-6 players. All ages.
Should not have
• Cartoons, characters, people

```html
<!DOCTYPE html>
<html lang="en">
<head>
<meta charset="utf-8">
<title>The Lock Box – Escape Room Flyer</title>
<link href="https://fonts.googleapis.com/css2?family=Big+Shoulders+Display:wght@800&family=Oswald:wght@500;600&family=Saira+Condensed:wght@400&display=swap" rel="stylesheet">
<style>
  :root {
    --ink: #050505;
    --gold: #e9c16e;
    --gold-deep: #a5823e;
    --gold-muted: #9c7f45;
    --maze-dark: #1b1a17;
    --maze-mid: #3a382f;
    --text-light: #e6e6e6;
    --text-soft: #d6d6d6;
  }
  * { margin: 0; padding: 0; box-sizing: border-box; }
  html, body {
    width: 849px; height: 1200px; overflow: hidden;
    background: var(--ink);
  }
  .flyer {
    position: relative;
    width: 849px; height: 1200px;
    background: var(--ink);
    overflow: hidden;
    font-family: "Saira Condensed", "Arial Narrow", sans-serif;
  }
  .brand {
    position: absolute; left: 48px; top: 130px;
    width: 180px;
    display: flex; flex-direction: column; align-items: center; gap: 12px;
  }
  .brand-mark {
    width: 64px; height: 64px; border-radius: 50%;
    background: var(--gold);
  }
  .brand-name {
    font-family: "Oswald", "Arial Narrow", sans-serif;
    font-weight: 600; font-size: 28px; letter-spacing: 1px;
    color: var(--gold); text-transform: uppercase; white-space: nowrap;
  }
  .contact {
    position: absolute; right: 49px; top: 44px;
    text-align: right; color: var(--gold);
    font-family: "Oswald", "Arial Narrow", sans-serif; font-weight: 600;
  }
  .contact-phone {
    display: flex; align-items: center; justify-content: flex-end; gap: 12px;
    font-size: 37px; line-height: 44px; letter-spacing: 1px;
  }
  .contact-phone svg { width: 36px; height: 36px; }
  .contact-web { font-size: 21px; line-height: 24px; font-weight: 500; }
  .maze-band {
    position: absolute; left: 22px; top: 329px; width: 809px; height: 386px;
    background: radial-gradient(ellipse at center, var(--maze-mid) 0%, var(--maze-dark) 55%, var(--ink) 100%);
  }
  .question-mark {
    position: absolute; left: 260px; top: 148px; width: 326px; height: 474px;
    background: linear-gradient(180deg, var(--gold-muted) 0%, rgba(201,160,90,0.55) 100%);
    border-radius: 46% 46% 30% 30%;
    opacity: 0.85;
  }
  .tagline {
    position: absolute; top: 402px;
    font-family: "Big Shoulders Display", "Arial Narrow", sans-serif;
    font-weight: 800; font-size: 86px; line-height: 96px;
    text-transform: uppercase; color: var(--gold);
  }
  .tagline-enter { left: 100px; text-align: left; }
  .tagline-escape { right: 104px; text-align: right; }
  .game-facts {
    position: absolute; left: 0; right: 0; top: 724px;
    text-align: center; font-size: 35px; color: var(--text-light);
  }
  .pitch {
    position: absolute; left: 40px; right: 40px; top: 851px;
    text-align: center; font-size: 29px; line-height: 38.6px; color: var(--text-soft);
  }
  .bookings {
    position: absolute; left: 0; right: 0; top: 1116px;
    text-align: center;
    font-family: "Oswald", "Arial Narrow", sans-serif; font-weight: 600;
    font-size: 27px; color: var(--gold);
  }
</style>
</head>
<body>
<main class="flyer">
  <div class="brand">
    <span class="brand-mark"></span>
    <span class="brand-name">The Lock Box</span>
  </div>

  <div class="contact">
    <div class="contact-phone">
      <svg viewBox="0 0 36 36" aria-hidden="true">
        <circle cx="18" cy="18" r="16" fill="none" stroke="currentColor" stroke-width="2.5"/>
        <path d="M12 10c1-1 2.5-1 3 0l2 3.5c.4.8 0 1.6-.6 2l-1.2.9c.9 2 2.4 3.6 4.4 4.6l.9-1.2c.5-.6 1.3-.9 2-.5l3.4 2c1 .6 1 2 0 3l-1.6 1.4c-1 .9-2.4 1.1-3.6.6-4.6-2-8.2-5.6-10.1-10.2-.5-1.2-.2-2.6.7-3.5z" fill="currentColor"/>
      </svg>
      <span>0417 265 839</span>
    </div>
    <div class="contact-web">www.thelockboxhartwell.com</div>
  </div>

  <div class="maze-band" role="img" aria-label="Dark photograph of an aged metal maze viewed from above"></div>
  <div class="question-mark" role="img" aria-label="Large translucent gold stylised question mark"></div>

  <h1 class="tagline tagline-enter">Many<br>Will<br>Enter...</h1>
  <p class="tagline tagline-escape">Few<br>Will<br>Escape</p>

  <p class="game-facts">60 minute game. Team work. 2-6 players. All ages.</p>

  <p class="pitch">Whether you are having a night out with friends or family,<br>celebrating a special event, planning a team-building activity,<br>or simply wanting a diversion from the doldrums of your<br>workweek, The Lock Box will provide you an unforgettable<br>live-action gaming experience.</p>

  <p class="bookings">Bookings essential</p>
</main>
</body>
</html>
```